Business Card for plovrix

Create a Business Card with an existing logo for plovrix AG. We are a Information Technology company that does consulting and developing SW to automate business processes. The main colors are given from the logo.

Industry/Entity Type

Business

Requirements
Nice to have
• we use a a font style Century Gothic in our documents

```html
<!DOCTYPE html>
<html lang="en">
<head>
<meta charset="utf-8">
<title>plovrix AG – Business Card</title>
<link href="https://fonts.googleapis.com/css2?family=Questrial&display=swap" rel="stylesheet">
<style>
  :root {
    --page: #e4e4e2;
    --card: #f5f5f4;
    --ink: #3b3b3b;
    --ink-soft: #5a5a5a;
    --brand-blue: #2b79bf;
    --brand-green: #8cc43f;
    --rule: #2b79bf;
  }
  * { box-sizing: border-box; margin: 0; padding: 0; }
  html, body { width: 1200px; height: 900px; overflow: hidden; }
  body {
    background: var(--page);
    font-family: "Questrial", "Century Gothic", sans-serif;
    color: var(--ink);
    display: flex;
    align-items: center;
    justify-content: center;
    gap: 60px;
  }
  .card {
    width: 510px;
    height: 330px;
    background: var(--card);
    box-shadow: 0 2px 6px rgba(0,0,0,.12);
    position: relative;
  }
  /* front */
  .card--front .brand {
    position: absolute;
    left: 50%;
    top: 128px;
    transform: translateX(-50%);
    display: flex;
    align-items: center;
    gap: 16px;
  }
  .brand-dot {
    width: 46px; height: 46px;
    border-radius: 50%;
    background: var(--brand-blue);
  }
  .brand-name {
    font-size: 52px;
    color: var(--ink);
    letter-spacing: 1px;
    line-height: 1;
  }
  .card--front .web {
    position: absolute;
    right: 92px;
    top: 214px;
  }
  .web { color: var(--brand-blue); font-size: 15px; letter-spacing: .5px; }
  /* back */
  .card--back .brand {
    position: absolute;
    left: 40px;
    bottom: 48px;
    display: flex;
    flex-direction: column;
    align-items: flex-start;
    gap: 18px;
  }
  .card--back .brand-dot { width: 78px; height: 78px; margin-left: 20px; }
  .card--back .brand-name { font-size: 56px; }
  .details {
    position: absolute;
    left: 262px;
    top: 40px;
    width: 215px;
  }
  .person {
    display: flex;
    align-items: baseline;
    gap: 10px;
    padding-bottom: 8px;
    border-bottom: 1.5px solid var(--rule);
  }
  .person-name { font-size: 19px; color: var(--ink); }
  .person-role { font-size: 12px; color: var(--ink-soft); }
  .contact { list-style: none; margin-top: 8px; font-size: 12.5px; line-height: 1.45; color: var(--ink); }
  .contact li { display: flex; align-items: center; gap: 7px; }
  .contact svg { width: 10px; height: 10px; fill: var(--brand-blue); flex: none; }
  .address { margin-top: 18px; font-size: 12.5px; line-height: 1.45; color: var(--ink); font-style: normal; }
  .card--back .web { display: block; margin-top: 18px; padding-left: 48px; font-size: 13.5px; }
</style>
</head>
<body>
  <section class="card card--front" aria-label="Business card front">
    <div class="brand">
      <span class="brand-dot"></span>
      <span class="brand-name">plovrix</span>
    </div>
    <span class="web">www.plovrix.ch</span>
  </section>

  <section class="card card--back" aria-label="Business card back">
    <div class="brand">
      <span class="brand-dot"></span>
      <span class="brand-name">plovrix</span>
    </div>
    <div class="details">
      <div class="person">
        <span class="person-name">Lukas Berner</span>
        <span class="person-role">CEO</span>
      </div>
      <ul class="contact">
        <li>
          <svg viewBox="0 0 10 10" aria-hidden="true"><path d="M2 0.5 L4 2.5 L3 4 Q4 6 6 7 L7.5 6 L9.5 8 L8 9.5 Q4 9.5 0.5 2 Z"/></svg>
          +41 56 210 48 63
        </li>
        <li>
          <svg viewBox="0 0 10 10" aria-hidden="true"><path d="M2.5 0 H7.5 V10 H2.5 Z M3.5 1.5 V7.5 H6.5 V1.5 Z"/></svg>
          +41 79 402 65 17
        </li>
        <li>
          <svg viewBox="0 0 10 10" aria-hidden="true"><path d="M0 2 H10 V8.5 H0 Z M0.8 2.6 L5 5.6 L9.2 2.6 Z" fill-rule="evenodd"/></svg>
          lukas.berner@plovrix.ch
        </li>
      </ul>
      <address class="address">Lindenweg 7, 5400 Baden<br>Switzerland</address>
      <span class="web">www.plovrix.ch</span>
    </div>
  </section>
</body>
</html>
```